Luxury Van Wrap Design for Corvel Tide

Corvel Tide is a high-end company based in the Hamptons specializing in architectural glass and pool safety systems. Our services include frameless glass pool fences, glass railings, automatic pool covers, and removable mesh pool fences. The brand should feel luxury, coastal, clean, modern, and architectural. Think premium Hamptons aesthetic, not loud or overly commercial.

Vehicle Type:
Van wrap design for a work van. Please create a design that can be adapted to a standard cargo van.

Design Goal:
We want a wrap or spot graphics that looks upscale and professional while still clearly showing what we do. It should feel like a luxury home services brand that works on beautiful high-end homes. The wrap should be visually striking but minimal and refined.

Style Direction:
• Luxury and modern
• Clean, minimal, high-end
• Coastal / Hamptons inspired
• Architectural feel
• Sophisticated, not busy
• Premium branding, not playful or cartoonish

Color Direction:
• White vehicle base preferred
• Use dark navy, soft coastal blue, and stainless/silver tones
• Keep the palette elegant and restrained
• Avoid overly bright colors, neon tones, or anything that feels cheap

Design Elements to Consider:
• Flowing wave-inspired graphic element to subtly reference the Hamptons/waterfront lifestyle
• Architectural glass-inspired visuals or clean linework
• Minimal, polished layout with good use of negative space
• The wrap should feel premium from a distance and up close

Services to Feature:
Please include these services in a clean, well-organized way:
• Frameless Glass Pool Fences
• Glass Railings
• Automatic Pool Covers
• Removable Pool Safety Fences

Brand Messaging Ideas:
Possible supporting text
• Uncompromising Safety. Unobstructed Views.

Information to Include:
• Corvel Tide logo
• Website: corveltide.example
• Phone number
• Social handle if space allows: @corveltide

What We Want to Avoid:
• Overly crowded layouts
• Generic contractor-style wraps
• Cheap-looking gradients
• Cartoon water splashes or clipart
• Too many photos
• Anything flashy, aggressive, or low-end

Wrap Preference:
We are open to:
• Partial wrap
• Spot graphics
But the overall design must still feel luxury and refined, not overdone.

Creative Notes:
The van should look like it belongs in front of a multi-million-dollar Hamptons home. The design should attract attention in an elegant way and appeal to architects, builders, designers, and high-end homeowners. Clean typography and strong layout are very important.

Deliverables:
• van wrap concept
• Both sides, rear, and hood if applicable
• Print-ready layout preferred
• Please show mockups on a 2012 Valtor K380 cargo van and a 2026 Valtor R470 Medium Roof Cargo Van

```html
<!DOCTYPE html>
<html lang="en">
<head>
<meta charset="utf-8">
<title>Corvel Tide — Van Wrap Side Panel</title>
<link rel="stylesheet" href="https://fonts.googleapis.com/css2?family=Oswald:wght@600&family=Montserrat:wght@400;700&family=Roboto+Condensed:wght@500&display=swap">
<style>
  :root {
    --page: #ffffff;
    --wrap-white: #ffffff;
    --panel-edge: #d9dcdf;
    --silver: #8e9295;
    --silver-dark: #7b7f82;
    --coastal-blue: #33789f;
    --charcoal: #3a3c3e;
    --rocker: #111213;
    --ink: #1c1c1c;
  }
  html, body {
    margin: 0;
    width: 1200px;
    height: 797px;
    overflow: hidden;
    background: var(--page);
  }
  .wrap-canvas { display: block; width: 1200px; height: 797px; }
  .panel-outline { fill: none; stroke: var(--panel-edge); stroke-width: 1.5; }
  .band-silver { fill: var(--silver); }
  .band-white { fill: var(--wrap-white); }
  .band-blue { fill: var(--coastal-blue); }
  .band-rocker { fill: var(--rocker); }
  .rule { stroke: var(--silver); stroke-width: 3; }
  .brand-name {
    font-family: "Oswald", sans-serif;
    font-weight: 600;
    font-size: 80px;
    fill: var(--silver-dark);
  }
  .brand-line {
    font-family: "Roboto Condensed", sans-serif;
    font-weight: 500;
    font-size: 20px;
    fill: var(--charcoal);
  }
  .slogan {
    font-family: "Montserrat", sans-serif;
    font-weight: 400;
    font-size: 16px;
    fill: #ffffff;
  }
  .services {
    font-family: "Montserrat", sans-serif;
    font-weight: 400;
    font-size: 13.5px;
    fill: #ffffff;
  }
  .phone {
    font-family: "Montserrat", sans-serif;
    font-weight: 700;
    font-size: 19px;
    fill: var(--ink);
  }
  .website {
    font-family: "Montserrat", sans-serif;
    font-weight: 400;
    font-size: 16px;
    fill: var(--ink);
  }
  .handle {
    font-family: "Montserrat", sans-serif;
    font-weight: 400;
    font-size: 11px;
    fill: var(--coastal-blue);
  }
  .handle-dot { fill: var(--coastal-blue); }
</style>
</head>
<body>
<svg class="wrap-canvas" viewBox="0 0 1200 797" xmlns="http://www.w3.org/2000/svg" aria-label="Corvel Tide van wrap side layout">
  <defs>
    <clipPath id="panel-shape">
      <rect x="120" y="200" width="980" height="320" rx="18"/>
    </clipPath>
  </defs>

  <g clip-path="url(#panel-shape)">
    <rect class="band-white" x="120" y="200" width="980" height="320"/>
    <g class="diagonal-bands" transform="rotate(-10.3 482 375)">
      <rect class="band-silver" x="-200" y="-200" width="1600" height="490"/>
      <rect class="band-blue" x="-200" y="422" width="1600" height="400"/>
      <g class="slogan-block">
        <text class="slogan" x="540" y="266">Uncompromising Safety.</text>
        <text class="slogan" x="545" y="285">Unobstructed Views.</text>
      </g>
      <text class="brand-name" x="478" y="372" textLength="520" lengthAdjust="spacingAndGlyphs">CORVEL TIDE</text>
      <line class="rule" x1="480" y1="384" x2="1010" y2="384"/>
      <text class="brand-line" x="484" y="412" textLength="530" lengthAdjust="spacing">ARCHITECTURAL GLASS &amp; POOL SAFETY SYSTEMS</text>
      <g class="services-list">
        <text class="services" x="686" y="445" textLength="300" lengthAdjust="spacingAndGlyphs">· Frameless Glass Pool Fences · Glass Railings</text>
        <text class="services" x="690" y="464" textLength="360" lengthAdjust="spacingAndGlyphs">· Automatic Pool Covers · Removable Pool Safety Fences</text>
      </g>
    </g>
    <rect class="band-rocker" x="120" y="470" width="980" height="50"/>
    <rect class="band-blue" x="366" y="494" width="432" height="16"/>
  </g>
  <rect class="panel-outline" x="120" y="200" width="980" height="320" rx="18"/>

  <g class="contact-block">
    <text class="phone" x="300" y="389">555-301-7420</text>
    <text class="website" x="300" y="407">corveltide.example</text>
    <circle class="handle-dot" cx="331" cy="418" r="5"/>
    <text class="handle" x="340" y="422">@corveltide</text>
  </g>
</svg>
</body>
</html>
```